Torvenu Business Card Design Project

We need a business card design for torvenu.com a company based in Berlin, Germany.

?Torvenu is marketplace that enables people all over the world to monetize and exchange their individual knowledge and language skills through interactive video sessions. User are matched by their interests.

On Torvenu everybody can be student or teacher (seller or buyer).

We would love to see designs that use or main color blue and green. The design should communicate what Torvenu enables - see my notice above.

Looking so forward to your designs
Cheers from Berlin,
Konrad

Target Market(s)

globally

Industry/Entity Type

Teacher

Requirements
Must have
• Konrad Wielert
CEO
Torvenu.com

Torvenu e-Services GmbH
Lindgrubweg 27
10117 Berlin

Fon: +49 30 481 906 27 14
Mobile: 49 171 57 04 91 3
E-Mail: k.wielert@torvenu.com
Web: www.torvenu.com

```html
<!DOCTYPE html>
<html lang="en">
<head>
<meta charset="utf-8">
<title>Torvenu Business Card</title>
<link rel="stylesheet" href="https://fonts.googleapis.com/css2?family=Didact+Gothic&display=swap">
<style>
  :root {
    --backdrop: #e4e4e6;
    --brand-blue: #1ea0dc;
    --brand-green: #8cbf2a;
    --card-white: #f7f7f7;
    --ink-grey: #6b6b6b;
    --rule-grey: #c9c9c9;
    --ghost-grey: #e9e9e9;
  }
  * { box-sizing: border-box; margin: 0; padding: 0; }
  html, body {
    width: 1200px;
    height: 900px;
    overflow: hidden;
    background: var(--backdrop);
    font-family: "Didact Gothic", "Century Gothic", sans-serif;
  }
  .canvas {
    position: relative;
    width: 1200px;
    height: 900px;
  }
  .card {
    position: absolute;
    width: 560px;
    height: 320px;
    border-radius: 3px;
    box-shadow: 0 10px 24px rgba(0,0,0,0.18);
    overflow: hidden;
  }
  /* Front side */
  .card--front {
    left: 80px;
    top: 100px;
    background: var(--brand-blue);
    display: flex;
    align-items: center;
    justify-content: center;
  }
  .wordmark {
    display: flex;
    align-items: center;
    gap: 16px;
  }
  .wordmark__square {
    width: 46px;
    height: 46px;
    background: #ffffff;
  }
  .wordmark__name {
    font-size: 74px;
    line-height: 1;
    color: #ffffff;
    letter-spacing: 1px;
  }
  /* Back side */
  .card--back {
    left: 560px;
    top: 480px;
    background: var(--card-white);
  }
  .card--back .wordmark {
    position: absolute;
    left: 40px;
    top: 132px;
    gap: 10px;
  }
  .card--back .wordmark__square {
    width: 26px;
    height: 26px;
    background: var(--brand-blue);
  }
  .card--back .wordmark__name {
    font-size: 40px;
    color: var(--ink-grey);
    letter-spacing: 0.5px;
  }
  .ghost-square {
    position: absolute;
    left: 50px;
    top: 236px;
    width: 110px;
    height: 110px;
    background: var(--ghost-grey);
  }
  .divider {
    position: absolute;
    left: 280px;
    top: 60px;
    width: 1px;
    height: 170px;
    background: linear-gradient(to bottom, transparent, var(--rule-grey) 20%, var(--rule-grey) 80%, transparent);
  }
  .contact {
    position: absolute;
    left: 300px;
    top: 52px;
    color: var(--ink-grey);
    font-size: 13px;
    line-height: 1.45;
  }
  .contact__name {
    font-size: 24px;
    line-height: 1.1;
    color: var(--ink-grey);
  }
  .contact__role {
    font-size: 20px;
    line-height: 1.1;
    color: var(--brand-blue);
    margin-bottom: 16px;
  }
  .contact__group { margin-bottom: 12px; }
  .contact__label { color: var(--brand-blue); }
</style>
</head>
<body>
  <main class="canvas">
    <section class="card card--front" aria-label="Business card front">
      <div class="wordmark">
        <span class="wordmark__square"></span>
        <span class="wordmark__name">torvenu</span>
      </div>
    </section>

    <section class="card card--back" aria-label="Business card back">
      <div class="ghost-square"></div>
      <div class="wordmark">
        <span class="wordmark__square"></span>
        <span class="wordmark__name">torvenu</span>
      </div>
      <div class="divider"></div>
      <div class="contact">
        <p class="contact__name">Konrad Wielert</p>
        <p class="contact__role">CEO</p>
        <div class="contact__group">
          <p><span class="contact__label">fon:</span> +49 30 481 906 27 14</p>
          <p><span class="contact__label">m:</span> 49 171 57 04 91 3</p>
        </div>
        <div class="contact__group">
          <p><span class="contact__label">e:</span> k.wielert@torvenu.com</p>
          <p><span class="contact__label">w:</span> www.torvenu.com</p>
        </div>
        <div class="contact__group">
          <p>Torvenu e-Services GmbH</p>
          <p>Lindgrubweg 27</p>
          <p>10117 Berlin</p>
        </div>
      </div>
    </section>
  </main>
</body>
</html>
```